I sell Finches---picture of White Finch Bird----

I raise and sell light color and white Finch - need card to give to Pet shops with my name - Lorna Pettigrew, address: 271 North Ardmore Ln. Santa Barbara, Ca. 93187 - phone - 805-479-3816. All birds raised and nourished in large outside aviary--very healthy and cared for. Would like card to be shiny red with bold print in Broadway font----purple bold print on red card. Design options open - you know best. Would like a picture or pictures of Finches - light or white in color.

Industry/Entity Type

Pet

Contact Information for Business Card

THE WREN KEEPER (LARGE, BOLD BROADWAY PRINT)

```html
<!DOCTYPE html>
<html lang="en">
<head>
<meta charset="utf-8">
<title>The Wren Keeper – Business Card</title>
<link rel="stylesheet" href="https://fonts.googleapis.com/css2?family=Limelight&family=Arimo:wght@400&display=swap">
<style>
  :root {
    --page-bg: #ecebee;
    --plum-glow: #a03f96;
    --violet: #6d37a2;
    --deep-violet: #56309b;
    --dusk-violet: #4a2a8c;
    --mist-pink: #f6e6f3;
    --blush: #dcb6de;
    --rose-light: #f1c9e6;
    --ink-white: #ffffff;
    --icon-ink: #6a36a0;
  }
  * { margin: 0; padding: 0; box-sizing: border-box; }
  html, body {
    width: 915px;
    height: 1200px;
    overflow: hidden;
    background: var(--page-bg);
  }
  .business-card {
    position: absolute;
    left: 157px;
    top: 88px;
    width: 600px;
    height: 1024px;
    overflow: hidden;
    background:
      radial-gradient(ellipse 70% 30% at 50% 4%, var(--plum-glow) 0%, rgba(160,63,150,0) 100%),
      linear-gradient(180deg, var(--violet) 0%, var(--deep-violet) 55%, var(--violet) 66%);
    color: var(--ink-white);
    text-align: center;
    font-family: "Arimo", Arial, sans-serif;
  }
  .brand-title {
    position: absolute;
    left: 0;
    right: 0;
    top: 88px;
    font-family: "Limelight", "Broadway", serif;
    font-weight: 400;
    font-size: 62px;
    line-height: 80px;
    letter-spacing: 1px;
  }
  .owner-name {
    position: absolute;
    left: 0;
    right: 0;
    top: 272px;
    font-size: 37px;
    letter-spacing: 0.5px;
  }
  .contact-icon {
    position: absolute;
    left: 272px;
    width: 56px;
    height: 56px;
  }
  .contact-icon.phone { top: 341px; }
  .contact-icon.pin { top: 461px; }
  .phone-number {
    position: absolute;
    left: 0;
    right: 0;
    top: 408px;
    font-size: 27px;
  }
  .street-address {
    position: absolute;
    left: 0;
    right: 0;
    top: 523px;
    font-size: 27px;
    line-height: 32px;
    font-style: normal;
  }
  .finch-photo {
    position: absolute;
    left: 0;
    right: 0;
    top: 650px;
    bottom: 0;
    background:
      radial-gradient(ellipse 30% 26% at 50% 42%, var(--rose-light) 0%, rgba(241,201,230,0.55) 45%, rgba(241,201,230,0) 100%),
      linear-gradient(180deg,
        rgba(109,55,162,0) 0%,
        var(--dusk-violet) 22%,
        var(--deep-violet) 45%,
        var(--blush) 66%,
        var(--mist-pink) 80%,
        var(--mist-pink) 100%);
  }
</style>
</head>
<body>
  <section class="business-card">
    <h1 class="brand-title">THE<br>WREN KEEPER</h1>
    <p class="owner-name">LORNA PETTIGREW</p>

    <svg class="contact-icon phone" viewBox="0 0 56 56" aria-hidden="true">
      <circle cx="28" cy="28" r="28" fill="var(--ink-white)"/>
      <rect x="20" y="14" width="16" height="28" rx="3" fill="none" stroke="var(--icon-ink)" stroke-width="2.6"/>
      <line x1="20" y1="19" x2="36" y2="19" stroke="var(--icon-ink)" stroke-width="2"/>
      <line x1="20" y1="36" x2="36" y2="36" stroke="var(--icon-ink)" stroke-width="2"/>
      <circle cx="28" cy="39" r="1.4" fill="var(--icon-ink)"/>
    </svg>
    <p class="phone-number">805-479-3816</p>

    <svg class="contact-icon pin" viewBox="0 0 56 56" aria-hidden="true">
      <circle cx="28" cy="28" r="28" fill="var(--ink-white)"/>
      <path d="M28 13c-6 0-10.5 4.6-10.5 10.3 0 7.4 10.5 19.7 10.5 19.7s10.5-12.3 10.5-19.7C38.5 17.6 34 13 28 13z" fill="var(--icon-ink)"/>
      <circle cx="28" cy="23.5" r="3.6" fill="var(--ink-white)"/>
    </svg>
    <address class="street-address">271 North Ardmore<br>Ln. Santa Barbara,<br>Ca. 93187</address>

    <div class="finch-photo" role="img" aria-label="Photograph of a pale white finch with a red beak standing on sandy ground against a soft purple background"></div>
  </section>
</body>
</html>
```